Complete Printing Package
Business Cards, Stationary, Envelopes, Presentation Folder
We love all the designs, but no one has submitted a minimalist design as mentioned in the brief. Very subtle color, only very light lines with thin stroke.
Anyone up for it?
We would just like something a little different to consider.
Notes:
1. We will not publish cell phone numbers on anything except business cards.
2. We will not publish email addresses on anything except business cards.
3. We like the look of "www.qtnx-build.com" stretched out to "w w w . q t n x - b u i l d . c o m"
4. On the green "H" element in the logo, there are some edge lines that define the H that we would like deleted when used as a watermark or shadow.
5. Can we see some concepts with the green shown as #8BA50B ?
Note to all:
We are looking for designs with straight lines throughout.
#78 & #79, can you change the black portions of your designs to gray?
Note to all, there seems to be many designs using black prominently throughout the design. We prefer the use of gray. We feel that the use of black is too harsh. If the designs look a little off with the black portion of the graphic in the logo, we are open to changing the black in the logo to gray as well.
Note to all, can you also include a fax cover page?
Note to all, I prefer a white background for the letterhead, envelopes and business cards.
For the proposal folder, we will consider grey, perhaps black and white backgrounds as well.
thanks!
Uploaded the template our printer uses for presentation folders. Please use this in preparing the presentation.
Thanks to all!

```html
<!DOCTYPE html>
<html lang="en">
<head>
<meta charset="utf-8">
<title>Quarrytonex Stationery Package</title>
<link href="https://fonts.googleapis.com/css2?family=Montserrat:wght@400;700&display=swap" rel="stylesheet">
<style>
  :root {
    --green: #8ba50b;
    --green-soft: #a3bb35;
    --gray: #4a4a4a;
    --gray-dark: #3d3d3d;
    --gray-line: #c9c9c9;
    --faint: #f0f0ee;
    --paper: #ffffff;
    --stage: #ece9e4;
  }
  * { box-sizing: border-box; margin: 0; padding: 0; }
  html, body { width: 1200px; height: 418px; overflow: hidden; }
  body { background: var(--stage); font-family: "Montserrat", sans-serif; color: var(--gray); position: relative; }
  .sheet { position: absolute; background: var(--paper); box-shadow: 0 1px 3px rgba(0,0,0,.18); overflow: hidden; }
  .brand { display: flex; align-items: center; gap: 3px; font-weight: 700; color: var(--gray); letter-spacing: .5px; white-space: nowrap; }
  .brand .mark { width: 7px; height: 7px; background: var(--green); flex: none; }
  .brand.on-green { color: var(--paper); }
  .brand.on-green .mark { background: var(--paper); }
  .watermark { position: absolute; left: 0; right: 0; text-align: center; font-weight: 700; color: var(--faint); letter-spacing: .5px; white-space: nowrap; }
  .web { position: absolute; left: 0; right: 0; text-align: center; font-size: 4px; color: #999; white-space: nowrap; }

  /* business cards */
  .card { top: 28px; width: 42px; height: 25px; display: flex; flex-direction: column; align-items: center; justify-content: center; gap: 2px; }
  .card .brand { font-size: 3.5px; gap: 2px; letter-spacing: .2px; }
  .card .brand .mark { width: 3.5px; height: 3.5px; }
  .card .line { font-size: 3px; color: #888; white-space: nowrap; }
  .card.green { background: var(--green); }

  /* letterheads */
  .letterhead { top: 90px; width: 136px; height: 274px; }
  .letterhead .brand { position: absolute; top: 12px; left: 50%; transform: translateX(-50%); font-size: 6px; }
  .letterhead .rule { position: absolute; left: 10px; right: 10px; height: 1px; background: var(--gray-line); }
  .fax-table { position: absolute; top: 40px; left: 10px; width: 116px; border-collapse: collapse; font-size: 3.5px; }
  .fax-table td { border: .5px solid var(--gray-line); height: 7px; padding: 0 2px; }
  .contact { position: absolute; top: 80px; left: 10px; right: 10px; display: flex; justify-content: space-between; font-size: 3.5px; color: #888; }
  .contact span::before { content: ""; display: inline-block; width: 3px; height: 3px; border-radius: 50%; background: var(--green); margin-right: 1px; }
  .letterhead .watermark { font-size: 11px; top: 205px; }

  /* note sheet */
  .note { left: 463px; top: 62px; width: 124px; height: 178px; }
  .note .brand { position: absolute; top: 14px; left: 50%; transform: translateX(-50%); font-size: 5px; }
  .note .watermark { font-size: 10px; top: 120px; }

  /* envelopes */
  .envelope { width: 106px; height: 36px; }
  .envelope .flap { position: absolute; top: 0; left: 0; right: 0; height: 14px; }
  .envelope .brand { position: absolute; top: 4px; left: 50%; transform: translateX(-50%); font-size: 4px; }

  /* folder */
  .folder-cover { left: 749px; top: 43px; width: 192px; height: 341px; background: var(--green); }
  .folder-cover .watermark { color: var(--green-soft); font-size: 16px; top: 150px; }
  .folder-inside { left: 941px; top: 43px; width: 211px; height: 341px; }
  .folder-inside .brand { position: absolute; top: 22px; right: 18px; font-size: 8px; }
  .folder-inside .brand .mark { width: 9px; height: 9px; }
  .folder-inside .watermark { font-size: 16px; top: 110px; }
  .pocket { position: absolute; left: 941px; top: 232px; width: 211px; height: 152px; }
</style>
</head>
<body>

  <section class="business-cards" aria-label="Business cards">
    <div class="sheet card" style="left:66px"><div class="brand"><span class="mark"></span>QUARRYTONEX</div></div>
    <div class="sheet card" style="left:112px"><div class="line">Alex Morrow</div><div class="line">Project Manager</div></div>
    <div class="sheet card green" style="left:158px"><div class="brand on-green"><span class="mark"></span>QUARRYTONEX</div></div>
    <div class="sheet card" style="left:204px"><div class="brand"><span class="mark"></span>QUARRYTONEX</div></div>
  </section>

  <article class="sheet letterhead fax-cover" style="left:91px">
    <div class="brand"><span class="mark"></span>QUARRYTONEX</div>
    <table class="fax-table">
      <tr><td>To</td><td>From</td></tr>
      <tr><td>Fax</td><td>Date</td></tr>
      <tr><td>Pages</td><td>Re</td></tr>
    </table>
    <div class="contact"><span>Tel</span><span>Fax</span><span>Address</span><span>Email</span></div>
    <div class="watermark">QUARRYTONEX</div>
    <div class="rule" style="bottom:14px"></div>
    <div class="web" style="bottom:7px">w w w . q t n x - b u i l d . c o m</div>
  </article>

  <article class="sheet letterhead" style="left:240px">
    <div class="brand"><span class="mark"></span>QUARRYTONEX</div>
    <div class="watermark">QUARRYTONEX</div>
    <div class="contact" style="top:auto;bottom:20px"><span>Tel</span><span>Fax</span><span>Address</span><span>Email</span></div>
    <div class="rule" style="bottom:14px"></div>
    <div class="web" style="bottom:7px">w w w . q t n x - b u i l d . c o m</div>
  </article>

  <article class="sheet note">
    <div class="brand"><span class="mark"></span>QUARRYTONEX</div>
    <div class="watermark">QUARRYTONEX</div>
    <div class="web" style="bottom:6px">w w w . q t n x - b u i l d . c o m</div>
  </article>

  <section class="envelopes" aria-label="Envelopes">
    <div class="sheet envelope" style="left:451px;top:259px">
      <div class="flap" style="background:var(--green)"></div>
      <div class="brand on-green"><span class="mark"></span>QUARRYTONEX</div>
    </div>
    <div class="sheet envelope" style="left:566px;top:259px">
      <svg width="106" height="36" aria-hidden="true"><polyline points="0,0 53,18 106,0" fill="none" stroke="#ddd" stroke-width=".6"/></svg>
    </div>
    <div class="sheet envelope" style="left:451px;top:304px">
      <div class="flap" style="background:var(--gray-dark)"></div>
      <div class="brand on-green"><span class="mark" style="background:var(--green)"></span>QUARRYTONEX</div>
    </div>
    <div class="sheet envelope" style="left:566px;top:311px">
      <svg width="106" height="36" aria-hidden="true"><polyline points="0,0 53,18 106,0" fill="none" stroke="#ddd" stroke-width=".6"/></svg>
    </div>
  </section>

  <section class="folder" aria-label="Presentation folder">
    <div class="sheet folder-cover">
      <div class="watermark">QUARRYTONEX</div>
    </div>
    <div class="sheet folder-inside">
      <div class="brand"><span class="mark"></span>QUARRYTONEX</div>
      <div class="watermark">QUARRYTONEX</div>
    </div>
    <svg class="pocket" viewBox="0 0 211 152" aria-hidden="true">
      <polygon points="0,18 172,0 211,18 211,152 0,152" fill="#fbfbfb" stroke="#ddd" stroke-width=".6"/>
      <polyline points="146,44 162,56 178,44" fill="none" stroke="#ccc" stroke-width=".6"/>
    </svg>
  </section>

</body>
</html>
```